Professional violinist needs business cards

I am trying to attract the following jobs:
-private violin lessons (primarily classical)
-performance gigs (weddings, birthday parties, funerals, etc.)
-collaborations with other artists (studio recordings, performances)

I want to communicate that I have a very high standard of excellence for my work, but I also love people and celebrations.
Values/style words I like are:
love, joy, peace, fun, beauty, authenticity, excellence, warmth, refined/sleek, free spirited. If that's too confusing, just ignore :)

I will attach my favorite business card template that I could find on Canva. The lines are supposed to be like a music staff, which I think is really cool, but I also don't want it to look too busy. I like the simple black and white--I think it looks sharp--but I also am open to other ideas. I also have seen business cards with pictures included that looked great, so I attached an image that could be used as well.

I am also attaching a file that I made of my initials that could be used as a logo, but I'm not sure if it should be included.

Information on the card:
-My name (18 letters total)
-"violinist"
-phone number, email, website

Thank you!

```html
<!DOCTYPE html>
<html lang="en">
<head>
<meta charset="utf-8">
<title>Lena Marlowe – Violinist Business Card</title>
<link href="https://fonts.googleapis.com/css2?family=Raleway:wght@400;500;600&display=swap" rel="stylesheet">
<style>
  :root {
    --bg: #1c1c1c;
    --card-black: #050505;
    --card-grey: #2a2a2a;
    --white: #ffffff;
    --gold: #d9a63a;
    --rule-grey: #8a8a8a;
    --muted: #c9c9c9;
  }
  * { box-sizing: border-box; margin: 0; padding: 0; }
  html, body { width: 1200px; height: 900px; overflow: hidden; }
  body {
    background: var(--bg);
    font-family: "Raleway", Arial, sans-serif;
    position: relative;
  }
  .card {
    position: absolute;
    left: 250px;
    width: 700px;
    height: 400px;
    overflow: hidden;
    box-shadow: 0 10px 30px rgba(0,0,0,0.6);
  }
  .card-front { top: 35px; background: var(--card-black); }
  .card-back {
    top: 465px;
    background: linear-gradient(100deg, var(--card-black) 55%, var(--card-grey) 100%);
  }
  .card-lines { position: absolute; inset: 0; width: 100%; height: 100%; }

  .front-name {
    position: absolute;
    left: 40px;
    top: 167px;
    height: 66px;
    display: flex;
    align-items: center;
    font-size: 58px;
    font-weight: 600;
    color: var(--white);
    letter-spacing: 1px;
    line-height: 1;
    white-space: nowrap;
  }
  .front-web {
    position: absolute;
    right: 40px;
    bottom: 42px;
    font-size: 15px;
    color: var(--white);
    letter-spacing: 1.5px;
  }

  .portrait {
    position: absolute;
    left: 0; top: 0;
    width: 265px; height: 100%;
    background: linear-gradient(90deg, #f4f4f4 0%, #e3dcd6 30%, #6b4a36 55%, #111 100%);
  }
  .identity { position: absolute; left: 320px; top: 158px; }
  .identity-name {
    font-size: 32px;
    font-weight: 500;
    color: var(--gold);
    letter-spacing: 0.5px;
    white-space: nowrap;
  }
  .identity-role {
    font-size: 15px;
    color: var(--muted);
    margin-top: 2px;
  }
  .contacts {
    position: absolute;
    left: 350px;
    top: 282px;
    list-style: none;
  }
  .contact {
    display: flex;
    align-items: center;
    gap: 14px;
    font-size: 18px;
    color: var(--white);
    height: 27px;
    white-space: nowrap;
  }
  .contact-icon { width: 16px; height: 16px; fill: var(--gold); flex: none; }
</style>
</head>
<body>

  <section class="card card-front">
    <svg class="card-lines" viewBox="0 0 700 400" aria-hidden="true">
      <g stroke="#fff" stroke-width="4">
        <line x1="0" y1="30" x2="700" y2="30"/>
        <line x1="0" y1="95" x2="700" y2="95"/>
        <line x1="0" y1="165" x2="700" y2="165"/>
        <line x1="0" y1="235" x2="700" y2="235"/>
        <line x1="0" y1="305" x2="700" y2="305"/>
        <line x1="0" y1="372" x2="700" y2="372"/>
      </g>
    </svg>
    <div class="front-name">Lena Marlowe</div>
    <div class="front-web">www.yourwebsite.com</div>
  </section>

  <section class="card card-back">
    <div class="portrait" role="img" aria-label="Portrait photo of the violinist in a black dress holding her violin and bow"></div>
    <svg class="card-lines" viewBox="0 0 700 400" aria-hidden="true">
      <line x1="560" y1="150" x2="680" y2="150" stroke="var(--rule-grey)" stroke-width="1.5"/>
      <line x1="590" y1="178" x2="680" y2="178" stroke="var(--gold)" stroke-width="1.5"/>
      <line x1="420" y1="210" x2="680" y2="210" stroke="var(--rule-grey)" stroke-width="1.5"/>
      <line x1="560" y1="258" x2="690" y2="258" stroke="var(--rule-grey)" stroke-width="1.5"/>
      <line x1="600" y1="280" x2="690" y2="280" stroke="var(--rule-grey)" stroke-width="1.5"/>
      <line x1="610" y1="305" x2="690" y2="305" stroke="var(--rule-grey)" stroke-width="1.5"/>
    </svg>
    <div class="identity">
      <div class="identity-name">Lena Marlowe</div>
      <div class="identity-role">Violinist</div>
    </div>
    <ul class="contacts">
      <li class="contact">
        <svg class="contact-icon" viewBox="0 0 16 16" aria-hidden="true"><path d="M1 5c0-2 3-3 7-3s7 1 7 3v1h-3V5H4v1H1z M3 7h10l1 7H2z"/></svg>
        <span>012 3456 7890</span>
      </li>
      <li class="contact">
        <svg class="contact-icon" viewBox="0 0 16 16" aria-hidden="true"><path d="M1 3h14v10H1z M2 4l6 5 6-5" fill="none" stroke="var(--gold)" stroke-width="1.6"/></svg>
        <span>info@yourwebsite.com</span>
      </li>
      <li class="contact">
        <svg class="contact-icon" viewBox="0 0 16 16" aria-hidden="true"><circle cx="8" cy="8" r="6.5" fill="none" stroke="var(--gold)" stroke-width="1.6"/><path d="M1.5 8h13 M8 1.5c3 3 3 10 0 13 M8 1.5c-3 3-3 10 0 13" fill="none" stroke="var(--gold)" stroke-width="1.2"/></svg>
        <span>www.yourwebsite.com</span>
      </li>
    </ul>
  </section>

</body>
</html>
```